Pebble Grocer

Hope all is well!

Wanted to make business cards for my father. His name is Samir Haddad and owns convenience stores. I have attached logo :)

He does not want any title just simple name and phone. An email would be nice as well.

Samir Haddad
Cell: 413-555-0148
Store: 413-555-0192

Pebblegrocer518@mailnest.example

The design and style is totally up to you :) The colors we were looking for were the same as logo :)

```html
<!DOCTYPE html>
<html lang="en">
<head>
<meta charset="utf-8">
<title>Pebble Grocer – Business Card</title>
<link rel="stylesheet" href="https://fonts.googleapis.com/css2?family=Montserrat:wght@400;500;700&display=swap">
<style>
  :root {
    --backdrop: #d9d4cc;
    --card-front: #f9fafc;
    --card-back: #141414;
    --brand-red: #e8333b;
    --brand-navy: #243b80;
    --ink: #1b1b1b;
  }
  * { margin: 0; padding: 0; box-sizing: border-box; }
  html, body { width: 900px; height: 1200px; overflow: hidden; }
  body {
    background: var(--backdrop);
    font-family: "Montserrat", Arial, sans-serif;
    color: var(--ink);
    position: relative;
  }
  .card {
    position: absolute;
    left: 68px;
    width: 758px;
    border-radius: 28px;
    box-shadow: 0 6px 14px rgba(0,0,0,0.25);
  }
  .card--front { top: 133px; height: 440px; background: var(--card-front); }
  .card--back  { top: 638px; height: 450px; background: var(--card-back); }

  .accent-bar {
    position: absolute; left: 0; top: 139px;
    width: 10px; height: 48px; background: var(--brand-red);
  }
  .holder-name {
    position: absolute; left: 45px; top: 145px;
    font-size: 26px; font-weight: 700; color: var(--brand-red);
    letter-spacing: 0.3px; line-height: 32px;
  }
  .address {
    position: absolute; left: 45px; top: 207px;
    font-size: 15px; line-height: 21px;
  }
  .contact-list {
    position: absolute; left: 41px; top: 267px;
    list-style: none; font-size: 16px;
  }
  .contact-list li {
    display: flex; align-items: center; height: 24px; white-space: nowrap;
  }
  .contact-list svg { width: 16px; height: 16px; margin-right: 13px; fill: var(--brand-red); flex: none; }

  .brand-name {
    position: absolute; font-weight: 700;
    white-space: nowrap; text-align: center;
  }
  .card--front .brand-name {
    left: 390px; width: 340px; top: 220px; font-size: 36px; color: var(--brand-navy);
  }
  .card--back .brand-name {
    left: 100px; width: 558px; top: 185px; font-size: 62px; color: var(--brand-red);
  }
</style>
</head>
<body>
  <section class="card card--front">
    <div class="accent-bar"></div>
    <h1 class="holder-name">Samir Haddad</h1>
    <p class="address">275 N. 400 W. Suite 9 Salt<br>Lake City, UT 84103</p>
    <ul class="contact-list">
      <li>
        <svg viewBox="0 0 16 16" aria-hidden="true"><path d="M2 6c0-2 2-3 6-3s6 1 6 3v1h-3V5.5H5V7H2zM4 8h8l2 5H2zM8 9.3a1.6 1.6 0 1 0 0 3.2 1.6 1.6 0 0 0 0-3.2z"/></svg>
        413-555-0192
      </li>
      <li>
        <svg viewBox="0 0 16 16" aria-hidden="true"><path d="M5 1h6a1 1 0 0 1 1 1v12a1 1 0 0 1-1 1H5a1 1 0 0 1-1-1V2a1 1 0 0 1 1-1zm.3 1.5v10h5.4v-10zM8 13.2a.6.6 0 1 0 0 1.2.6.6 0 0 0 0-1.2z"/></svg>
        413-555-0148
      </li>
      <li>
        <svg viewBox="0 0 16 16" aria-hidden="true"><path d="M1 4h14v1L8 9.5 1 5zm0 2.2 7 4.5 7-4.5V12H1z"/></svg>
        Pebblegrocer518@mailnest.example
      </li>
    </ul>
    <div class="brand-name">Pebble Grocer</div>
  </section>

  <section class="card card--back">
    <div class="brand-name">Pebble Grocer</div>
  </section>
</body>
</html>
```